Flyer Design - You Need a Mobile Website

We need an A4 size flyer design for print to be used as part of a Direct Mail package.

The target audience is small business owners, such as Vets, Dentists, Plumbers and others who would benefit from owning a Mobile Website.

"You're not fully open for business until you have a mobile website." is the theme.

Our product is a mobile-phone/smartphone optimized version of the client's normal desktop website, automatically updated as the main web-site is changed.

The desired course of action is for the reader to go to the website and order a FREE preview.

IMPORTANT NOTE: 4-9-2013 we have revieds some of the wording see File4 "Get your Mobile Website Built Free of charge"

Target Market(s)

Small Business Owners, businesses that provide emergency/urgent services. (eg Vets, Dentist, Plumber etc)

Industry/Entity Type

Small Business

Requirements
Must have
• Design must comply with the printers specification for A4 flyers, details are here: http://www.printvarolo.com.au/Templates/A4Templates/tabid/142/default.aspx
(Photoshop version is attached)

Proposed Text is attached (see attachment 1 "You're not fully open for business until you have a mobile website")
Nice to have
• Further background explanation is attached. (see attachment 2 "Brindlecove Mobile Websites Flyer-Explanation")

```html
<!DOCTYPE html>
<html lang="en">
<head>
<meta charset="utf-8">
<title>Mobile Website Flyer</title>
<link rel="stylesheet" href="https://fonts.googleapis.com/css2?family=Nunito:wght@700;800;900&family=Open+Sans:wght@400;600;700&display=swap">
<style>
:root{
  --page:#e9ebee;
  --sheet-top:#ffffff;
  --sheet-bottom:#d9dee6;
  --headline-blue:#3d80c2;
  --headline-navy:#1c2f6a;
  --ink:#1e1e1e;
  --brand-blue:#3f7fc0;
  --panel-blue:#3a75b4;
  --white:#ffffff;
}
*{box-sizing:border-box;margin:0;padding:0}
html,body{width:1200px;height:1000px;overflow:hidden;background:var(--page)}
body{font-family:"Open Sans",Arial,sans-serif;color:var(--ink)}
.flyer{position:absolute;left:267px;top:30px;width:666px;height:940px;overflow:hidden;
  background:linear-gradient(180deg,var(--sheet-top) 0%,#f3f5f8 40%,var(--sheet-bottom) 78%);
  box-shadow:0 2px 10px rgba(0,0,0,.25)}
.abs{position:absolute}
.headline{left:30px;top:34px;font-family:"Nunito",Arial,sans-serif;font-weight:800;color:var(--headline-blue);font-size:29px;line-height:38px;letter-spacing:.2px}
.headline strong{display:block;font-weight:900;color:var(--headline-navy);font-size:45px;line-height:50px;margin-top:2px}
.intro{left:30px;top:166px;width:350px;font-size:12px;line-height:18px}
.stats{left:30px;top:246px;font-size:12px;line-height:23px}
.stats b{font-weight:700}
.stats .source{font-size:11.5px}
.hero-phone{left:440px;top:30px;width:226px;height:278px;border-radius:22px 0 0 22px;
  background:linear-gradient(160deg,#2a2a2c 0%,#4c7fbb 35%,#3f73b1 60%,#e9c8aa 82%,#f1d6bd 100%)}
.col-label{font-weight:700;font-size:15px;color:var(--headline-navy);top:378px}
.thumb{top:404px;width:76px;height:146px;border-radius:10px;background:linear-gradient(180deg,#1f1f1f 0%,#5b88c0 30%,#dfe7f1 60%,#1f1f1f 100%)}
.versus{left:128px;top:450px;font-family:"Nunito",Arial,sans-serif;font-weight:800;font-size:42px;color:var(--brand-blue)}
.points{list-style:none;font-size:12px;font-weight:700;line-height:18px}
.points li{position:relative;padding-left:16px;margin-bottom:4px}
.points li.dot::before{content:"";position:absolute;left:1px;top:5px;width:8px;height:8px;border-radius:50%;background:var(--brand-blue)}
.chart{left:436px;top:348px}
.why{left:422px;top:464px;width:224px;height:280px;border-radius:10px;background:var(--panel-blue);color:var(--white);padding:14px 10px 10px 10px}
.why h2{font-size:14px;font-weight:700;margin-bottom:6px}
.why ul{list-style:none;font-size:11.3px;font-weight:600;line-height:16px}
.why li{margin-bottom:5.5px}
.wave{left:0;top:652px}
.badge{left:16px;top:690px;width:144px;height:144px}
.badge-text{left:16px;top:690px;width:144px;height:144px;display:flex;flex-direction:column;align-items:center;justify-content:center;color:var(--white);font-weight:700;font-size:13px;line-height:16px;text-align:center}
.badge-text .big{font-size:19px;line-height:20px}
.cta{left:183px;top:780px;width:468px;color:var(--white);font-size:11.4px;line-height:16px}
.cta b{font-weight:700}
.company{left:30px;top:850px;color:var(--white);font-size:11.3px;line-height:18px}
.company .name{font-weight:700;font-size:11.8px}
.company b{font-weight:700}
.established{left:380px;top:904px;color:var(--white);font-size:12px;font-weight:700}
.brand{right:18px;top:848px;display:flex;align-items:center;gap:6px;color:var(--white);font-weight:700;font-size:14px}
.brand .square{width:16px;height:16px;background:var(--brand-blue)}
.site{right:16px;top:905px;color:var(--white);font-size:11.5px;font-weight:700}
</style>
</head>
<body>
<main class="flyer">
  <h1 class="abs headline">You´re not fully open for<br>business until you have a<strong>mobile website</strong></h1>

  <p class="abs intro">More than half of all Australians are using their mobile phones to access the web. That means that half of your customers are too. Now, all businesses need a Mobile Website just to keep up with their competitors.</p>

  <div class="abs stats">
    <p>In 2012 Australian Smartphone users accessed the internet:</p>
    <p><b>&gt; 62% looked for information on products and services</b></p>
    <p><b>&gt; 55% looked for suppliers of products or services</b></p>
    <p><b>&gt; 33% ordered goods or services</b></p>
    <p class="source">(source: Hallvale Research 2012)</p>
  </div>

  <div class="abs hero-phone" role="img" aria-label="Hand holding a smartphone whose screen reads Searching for dental clinic with a 45% loading ring"></div>

  <span class="abs col-label" style="left:30px">Standard Website</span>
  <span class="abs col-label" style="left:205px">Mobile Website</span>
  <div class="abs thumb" style="left:30px" role="img" aria-label="Smartphone showing a full desktop website shrunk to fit"></div>
  <span class="abs versus">v/s</span>
  <div class="abs thumb" style="left:205px" role="img" aria-label="Smartphone showing a mobile optimised website with call and map buttons"></div>

  <ul class="abs points" style="left:26px;top:555px;width:160px">
    <li class="dot">Text is too small.</li>
    <li class="dot">Must Pinch, zoom and scroll to read.</li>
    <li class="dot">Links are too small for touch navigation</li>
  </ul>
  <ul class="abs points" style="left:198px;top:552px;width:215px">
    <li class="dot">Finger friendly navigation easy too use</li>
    <li class="dot">Click to call button, makes it easy for customers to contact you directly</li>
    <li class="dot">Mobile maps with find us button</li>
    <li>Automatically updates when you change your regular website</li>
    <li>Works on All Smartphones.</li>
  </ul>

  <svg class="abs chart" width="200" height="112" viewBox="0 0 200 112" aria-label="Bar chart of mobile web use 2009 to 2013">
    <g fill="#3f7fc0">
      <rect x="4" y="72" width="30" height="36"/>
      <rect x="42" y="45" width="30" height="63"/>
      <rect x="80" y="32" width="30" height="76"/>
      <rect x="118" y="23" width="30" height="85"/>
      <rect x="156" y="14" width="30" height="94"/>
    </g>
    <g font-family="Open Sans, Arial, sans-serif" font-size="10" font-weight="700" text-anchor="middle" fill="#1e1e1e">
      <text x="19" y="68">2009</text><text x="57" y="41">2010</text><text x="95" y="28">2011</text><text x="133" y="19">2012</text><text x="171" y="11">2013</text>
    </g>
    <g font-family="Open Sans, Arial, sans-serif" font-size="10" font-weight="700" text-anchor="middle" fill="#ffffff">
      <text x="19" y="103">25</text><text x="57" y="103">41</text><text x="95" y="103">50</text><text x="133" y="103">58</text><text x="171" y="103">64</text>
    </g>
  </svg>

  <svg class="abs wave" width="666" height="288" viewBox="0 0 666 288" aria-hidden="true">
    <defs>
      <linearGradient id="footerShade" x1="0" y1="0" x2="0" y2="1">
        <stop offset="0" stop-color="#5a5a5d"/><stop offset="1" stop-color="#2c2c2e"/>
      </linearGradient>
    </defs>
    <path d="M0 28 C150 70 400 102 666 104 L666 116 C400 114 150 82 0 40 Z" fill="#2a5ea4"/>
    <path d="M0 40 C150 82 400 114 666 116 L666 288 L0 288 Z" fill="url(#footerShade)"/>
  </svg>

  <section class="abs why">
    <h2>Why get a Mobile Webite?</h2>
    <ul>
      <li>&gt; To get more website traffic*.</li>
      <li>&gt; To Boost your brand</li>
      <li>&gt; To Generate new leads</li>
      <li>&gt; To Increase sales and revenue.</li>
      <li>&gt; To avoid frustrating your audience</li>
      <li>&gt; To step into the digital age</li>
      <li>&gt; To stay ahead of the competition</li>
      <li>&gt; (*Adding a mobile friendly site results in an overall traffic increase of 18% (source: Corbett Analytics)</li>
    </ul>
  </section>

  <svg class="abs badge" viewBox="0 0 144 144" aria-hidden="true">
    <polygon fill="#3a86cc" stroke="#2a6aa8" stroke-width="2" points="142,72 130.9,83.7 136.7,98.8 121.9,105.4 121.5,121.5 105.4,121.9 98.8,136.7 83.7,130.9 72,142 60.3,130.9 45.2,136.7 38.6,121.9 22.5,121.5 22.1,105.4 7.3,98.8 13.1,83.7 2,72 13.1,60.3 7.3,45.2 22.1,38.6 22.5,22.5 38.6,22.1 45.2,7.3 60.3,13.1 72,2 83.7,13.1 98.8,7.3 105.4,22.1 121.5,22.5 121.9,38.6 136.7,45.2 130.9,60.3"/>
  </svg>
  <div class="abs badge-text"><span>Get a</span><span>Mobile Website</span><span class="big">FREE</span><span>Preview NOW!</span></div>

  <p class="abs cta">go to <b>http://www.brindlecove.com.au/offer</b> to order you new Mobile Website Preview. Within a few hours Brindlecove will build your new Mobile Website ready for you to Preview; Totally FREE to you. (Normally $199 value)</p>

  <div class="abs company">
    <p class="name">BRINDLECOVE CORPORATION Pty Ltd</p>
    <p>ABN 12 345 678 901</p>
    <p>Level 3, 48 Wattle Lane Melbourne – P.O. Box 902 Eastbrook Victoria 3199</p>
    <p>Phone: <b>03 9000 4417</b>, Email: <b>admin@brindlecove.com.au</b></p>
  </div>
  <span class="abs established">Established 1999</span>
  <div class="abs brand"><span class="square"></span><span>Brindlecove</span></div>
  <span class="abs site">www.brindlecove.com.au</span>
</main>
</body>
</html>
```